Website for vegan focused blog

A website is needed so that I can launch my new blog in Dubai. It will be mainly vegan focused but also lifestyle based. Wordpress based- i started to build a site on Wordpress but design is not my forte ;)
Main content on the site will be; my recipes, reviews of products/restaurants, lifestyle posts and travel.
For this I ask for a homepage design, a recipe design page that includes a recipe card and a generic page for posts that can show pictures and videos. Also a contact me page.
Main headers should be: Home, Recipes and happy for suggestions.
Must look clean and neat but appealing, happy for minimalist look. I like pink and grey colours. Must be Wordpress compatible.
Have attached a couple of example posts for reference
Must have social links etc.
name of blog is: Maddie on the dunes
Other blogs I like are: https://sparsekitchen.example/ https://thyleafshines.example/ https://thyleafshines.example/ https://www.ohladycakes.com/https://lentilsforsupper.example/ https://jorunbeck.example/

Target Market(s)

Residents in the UAE. General individuals interested in vegan meals, plant based nutrition, travel and reviews.

Number of Pages Required

4 page

Colors
eea4c8
eda3c7
f9d9e8
dbdbdb
aaaaaa
d5d5d5

Requirements
Must have
• Recipe page- must include recipe card plug in option
• Social media integration
• Email sign ups

```html
<!DOCTYPE html>
<html lang="en">
<head>
<meta charset="utf-8">
<title>Mushroom Steak – Maddie on the dunes</title>
<link href="https://fonts.googleapis.com/css2?family=Playfair+Display:ital,wght@0,400;1,400&family=Lato:wght@400;700&display=swap" rel="stylesheet">
<style>
:root{
  --pink:#eea4c8;
  --pink-soft:#f9d9e8;
  --ink:#333333;
  --text:#555555;
  --muted:#aaaaaa;
  --line:#dbdbdb;
  --line-soft:#e9e9e9;
  --footer:#f7f7f7;
  --button:#666666;
  --food:linear-gradient(135deg,#2f4a22 0%,#3d5a2a 25%,#5a3324 45%,#7a3a2a 60%,#c9412e 75%,#ece4da 100%);
}
*{box-sizing:border-box;margin:0;padding:0}
html,body{width:1200px;height:2620px;overflow:hidden;background:#fff}
body{position:relative;font-family:'Lato',sans-serif;color:var(--text);font-size:10px;line-height:1.6}
.abs{position:absolute}
.serif{font-family:'Playfair Display',serif}
.photo{background:var(--food)}

/* header */
.brand{left:0;width:1200px;top:28px;text-align:center;font-family:'Playfair Display',serif;font-size:40px;color:var(--pink);line-height:48px}
.nav{left:0;top:114px;width:1200px;height:38px;border-top:1px solid var(--line-soft);border-bottom:1px solid var(--line-soft)}
.nav a{position:absolute;top:10px;font-family:'Playfair Display',serif;font-style:italic;font-size:12px;color:var(--ink);text-decoration:none;transform:translateX(-50%)}
.nav svg{position:absolute;left:955px;top:12px}

/* article */
.post-title{left:234px;width:507px;top:196px;text-align:center;font-family:'Playfair Display',serif;font-size:19px;color:var(--pink)}
.post-rule{left:472px;top:231px;width:30px;height:1px;background:var(--line)}
.post-date{left:234px;width:507px;top:241px;text-align:center;font-size:7px;letter-spacing:1.5px;color:var(--muted)}
.hero{left:234px;top:274px;width:507px;height:353px}
.slide-arrow{position:absolute;top:166px;width:26px;height:22px;background:rgba(120,120,120,.55);display:flex;align-items:center;justify-content:center}
.post-body{left:234px;top:640px;width:507px;font-size:9.5px;line-height:15px;color:var(--ink)}
.post-body p{margin-bottom:14px}
.post-meta{left:234px;top:842px;width:507px;height:42px;border-top:1px solid var(--line-soft);border-bottom:1px solid var(--line-soft);font-size:7.5px}
.post-meta .count{position:absolute;left:0;top:14px;color:var(--ink);letter-spacing:.5px}
.post-meta .divider{position:absolute;left:76px;top:8px;width:1px;height:26px;background:var(--line)}
.post-meta .tags{position:absolute;left:92px;top:14px;color:var(--muted)}
.post-meta .tags b{color:var(--ink);font-weight:400;letter-spacing:.5px}
.share{position:absolute;right:0;top:15px;display:flex;gap:8px}
.share i{display:block;width:7px;height:7px;border-radius:50%;background:var(--ink)}

/* recipe card */
.recipe-title{left:234px;top:918px;font-family:'Playfair Display',serif;font-size:18px;color:var(--pink)}
.stars{left:684px;top:924px;display:flex;gap:1px}
.times{left:234px;top:955px;width:320px;height:34px;border-top:1px solid var(--line-soft);border-bottom:1px solid var(--line-soft);display:flex}
.times div{flex:1;text-align:center;font-size:7px;color:var(--ink);padding-top:3px;line-height:12px;letter-spacing:.5px}
.times div+div{border-left:1px solid var(--line-soft)}
.times span{color:var(--muted);letter-spacing:0}
.recipe-photo{left:589px;top:950px;width:152px;height:105px}
.card-btn{top:1063px;height:17px;border:1px solid var(--line-soft);background:#f5f5f5;font-size:7px;letter-spacing:.5px;color:var(--ink);display:flex;align-items:center;justify-content:center;gap:4px}
.recipe-byline{left:234px;top:993px;font-size:8px;line-height:13px;color:var(--ink)}
.recipe-head{left:234px;font-size:9px;letter-spacing:1px;color:var(--ink)}
.ingredients{left:240px;top:1058px;width:320px;list-style:none;font-size:8px;line-height:13px;color:var(--ink)}
.instructions{left:240px;top:1227px;width:310px;padding-left:12px;font-size:8px;line-height:12.5px;color:var(--ink)}
.notes{left:234px;top:1398px;width:330px;font-size:8px;line-height:13px;color:var(--ink)}

/* prev / next */
.post-nav{left:234px;top:1464px;width:507px;height:33px;border-top:1px solid var(--line-soft);border-bottom:1px solid var(--line-soft);font-family:'Playfair Display',serif;font-style:italic;font-size:10px;color:var(--ink)}
.post-nav .prev{position:absolute;left:0;top:8px}
.post-nav .next{position:absolute;right:0;top:8px}

/* related */
.section-head{left:234px;width:507px;text-align:center;font-size:9px;letter-spacing:1.5px;color:var(--ink)}
.related{left:234px;top:1565px;width:507px;display:flex;justify-content:space-between}
.related-item{width:158px;text-align:center}
.related-item .photo{height:126px}
.related-item .date{margin-top:12px;font-size:6.5px;letter-spacing:1px;color:var(--muted)}
.related-item .title{margin-top:2px;font-family:'Playfair Display',serif;font-style:italic;font-size:9.5px;line-height:12px;color:var(--ink)}
.rule{left:234px;width:507px;height:1px;background:var(--line-soft)}

/* comments */
.comment{left:234px;width:507px}
.comment .avatar{position:absolute;left:0;top:0;width:45px;height:45px;border-radius:50%;background:var(--pink)}
.comment .name{position:absolute;top:2px;font-family:'Playfair Display',serif;font-size:10px;color:var(--ink)}
.comment .when{font-family:'Lato',sans-serif;font-size:6.5px;letter-spacing:.8px;color:var(--muted);margin-left:14px}
.comment .reply{position:absolute;right:0;top:4px;font-size:7px;letter-spacing:1px;color:var(--ink)}
.comment p{position:absolute;top:22px;font-size:8px;line-height:12.5px;color:var(--ink)}
.field{border:1px solid var(--line-soft);font-size:7.5px;color:var(--muted);padding:7px 10px}
.submit{left:608px;top:2322px;width:124px;height:30px;background:var(--button);color:#fff;font-size:8px;letter-spacing:1px;display:flex;align-items:center;justify-content:center}

/* sidebar */
.widget{left:777px;width:189px;border:1px solid var(--line-soft)}
.widget-title{position:absolute;left:12px;top:12px;font-family:'Playfair Display',serif;font-style:italic;font-size:11px;color:var(--pink)}
.about-photo{position:absolute;left:12px;top:46px;width:164px;height:96px;background:linear-gradient(180deg,#d8c7b8 0%,#a39590 40%,#4a4a52 75%,#2a2c33 100%)}
.about-text{position:absolute;left:14px;top:154px;width:160px;text-align:center;font-size:8px;line-height:12px;color:var(--ink)}
.more{position:absolute;left:0;width:187px;top:226px;text-align:center;font-size:7.5px;color:var(--ink)}
.socials{position:absolute;display:flex;gap:8px}
.socials i{display:block;width:18px;height:18px;border-radius:50%;background:var(--pink)}
.newsletter-input{position:absolute;left:12px;top:48px;width:164px;height:31px;border:1px solid var(--line-soft);font-size:7px;color:var(--muted);padding:10px 8px}
.pink-btn{position:absolute;left:12px;width:164px;height:26px;background:var(--pink-soft);color:#fff;font-size:7.5px;letter-spacing:1px;display:flex;align-items:center;justify-content:center}
.insta-grid{position:absolute;left:12px;top:46px;width:164px;display:grid;grid-template-columns:1fr 1fr;gap:3px}
.insta-grid .photo{height:81px}
.latest{position:absolute;left:12px;display:flex;gap:10px}
.latest .photo{width:56px;height:47px;flex:none}
.latest .t{font-family:'Playfair Display',serif;font-style:italic;font-size:8px;line-height:10px;color:var(--ink);margin-top:2px}
.latest .c{font-size:5.5px;letter-spacing:1px;color:var(--muted);margin-top:8px}

/* footer */
.footer{left:0;top:2420px;width:1200px;height:200px;background:var(--footer)}
.footer .brand{top:44px;font-size:36px}
.footer .socials{left:524px;top:113px}
.footer .socials i{width:20px;height:20px}
.copyright{position:absolute;left:0;width:1200px;top:176px;text-align:center;font-size:7px;color:var(--muted)}
</style>
</head>
<body>

<header>
  <div class="abs brand">Maddie on the dunes</div>
  <nav class="abs nav">
    <a style="left:351px">Home</a>
    <a style="left:416px">About</a>
    <a style="left:486px">Recipes</a>
    <a style="left:590px">Reviews of products</a>
    <a style="left:676px">Lifestyle</a>
    <a style="left:757px">Travel</a>
    <a style="left:844px">Contact</a>
    <svg width="12" height="12" viewBox="0 0 12 12"><circle cx="5" cy="5" r="3.6" fill="none" stroke="#333" stroke-width="1.6"/><line x1="7.6" y1="7.6" x2="11" y2="11" stroke="#333" stroke-width="1.8"/></svg>
  </nav>
</header>

<main>
  <h1 class="abs post-title">Mushroom Steak</h1>
  <div class="abs post-rule"></div>
  <div class="abs post-date">SATURDAY, SEPTEMBER 8, 2018</div>

  <div class="abs hero photo" role="img" aria-label="Photo of a sliced grilled portobello mushroom steak with roasted tomatoes, spinach and a creamy dip">
    <div class="slide-arrow" style="left:0"><svg width="12" height="6" viewBox="0 0 12 6"><path d="M12 3H1M3.5 .5 1 3l2.5 2.5" fill="none" stroke="#fff"/></svg></div>
    <div class="slide-arrow" style="right:0"><svg width="12" height="6" viewBox="0 0 12 6"><path d="M0 3h11M8.5 .5 11 3 8.5 5.5" fill="none" stroke="#fff"/></svg></div>
  </div>

  <div class="abs post-body">
    <p>Steak and vegan don't go in the same sentence BUT trust me on this...a decent sized Portobello shroom cooked just right with a blend of delicious marinade, it has the meatiest texture and its delicious as well oh and did we mention it is completely cruelty free!?</p>
    <p>To get the right texture you need the right tools so I always suggest cooking this on a griddle pan or even on the BBQ to give it that additional boost of flavours.</p>
    <p>When my non vegan friends are looking for something to cook when they have the plant powered team over for dinner, I always use this as a suggestion. The sides can be mixed and matched so in this instance I have used a grilled tomato and a pile of steamed spinach but you can add fries or salad or anything else that would be served alongside a steak. So all in all, it is a very versatile dish.</p>
  </div>

  <div class="abs post-meta">
    <span class="count">12 COMMENTS</span>
    <span class="divider"></span>
    <span class="tags"><b>TAGGED :</b> Food, mushroom, balsamic vinegar, olive oil, cumin, paprika, spinach</span>
    <div class="share"><i></i><i></i><i></i><i></i><i></i></div>
  </div>

  <section>
    <h2 class="abs recipe-title">Mushroom Steak</h2>
    <div class="abs stars">
      <svg width="57" height="11" viewBox="0 0 57 11">
        <g fill="#eea4c8"><path id="st" d="M5.5 .5l1.5 3.3 3.5.4-2.6 2.4.7 3.5-3.1-1.8-3.1 1.8.7-3.5L.5 4.2 4 3.8z"/><use href="#st" x="11.5"/><use href="#st" x="23"/><use href="#st" x="34.5"/></g>
        <use href="#st" x="46" fill="none" stroke="#eea4c8" stroke-width=".8"/>
      </svg>
    </div>
    <div class="abs times">
      <div>PREP TIME<br><span>◷ 10 mins</span></div>
      <div>COOK TIME<br><span>◷ 35 mins</span></div>
      <div>TOTAL TIME<br><span>◷ 45 mins</span></div>
    </div>
    <div class="abs recipe-photo photo" role="img" aria-label="Small photo of the finished mushroom steak plate"></div>
    <div class="abs card-btn" style="left:608px;width:54px">
      <svg width="7" height="7" viewBox="0 0 7 7"><rect x=".5" y=".5" width="6" height="6" fill="none" stroke="#333"/><rect x="2" y=".5" width="3" height="2" fill="#333"/></svg>SAVE</div>
    <div class="abs card-btn" style="left:672px;width:56px">
      <svg width="8" height="7" viewBox="0 0 8 7"><rect x="2" y="0" width="4" height="2" fill="#333"/><rect x="0" y="2" width="8" height="3" fill="#333"/><rect x="2" y="4" width="4" height="3" fill="#fff" stroke="#333" stroke-width=".6"/></svg>PRINT</div>

    <div class="abs recipe-byline">Autor : Rosalind Tarrow<br>Serves : 1</div>

    <h3 class="abs recipe-head" style="top:1038px">INGREDIENTS</h3>
    <ul class="abs ingredients">
      <li>1 large Portobello mushroom- cleaned well and destalked</li>
      <li>1 tbsp balsamic vinegar</li>
      <li>½ tbsp olive oil</li>
      <li>Pinch of cumin</li>
      <li>Pinch of salt and pepper</li>
      <li>Pinch paprika</li>
      <li>½ garlic clove minced</li>
      <li>250g Spinach</li>
      <li>1 large tomato- cut in half and seasoned</li>
      <li>Add chips, a jacket potato or any other sides.</li>
    </ul>

    <h3 class="abs recipe-head" style="top:1207px">INSTRUCTIONS</h3>
    <ol class="abs instructions">
      <li>Mix together the olive oil, balsamic vinegar, cumin, salt and pepper and paprika</li>
      <li>Add in the Portobello mushroom and marinate for 15 minutes, turning the mushroom over half way through</li>
      <li>Turn on the grill and place the tomato, seasoned on a baking tray for 10 minutes.</li>
      <li>Heat a non stick griddle pan to a medium heat and add the marinated mushroom to the pan. Cook on each side for 4 minutes or until it turns a beautiful caramelized colour.</li>
      <li>In the meantime steam or sauté the spinach</li>
      <li>Plate up the goodness and enjoy...simple as that!</li>
    </ol>

    <h3 class="abs recipe-head" style="top:1377px">NOTES</h3>
    <p class="abs notes">The dip that I used here was just a combination of vegan mayo, dash of lemon juice, fresh chopped basil and a ½ tsp of mustard.</p>
  </section>

  <nav class="abs post-nav">
    <span class="prev">←&nbsp;&nbsp;&nbsp;Pellentesque tempor efficitur auctor</span>
    <span class="next">Suspendisse nec tempus erat&nbsp;&nbsp;&nbsp;→</span>
  </nav>

  <h2 class="abs section-head" style="top:1530px">RELATED POSTS</h2>
  <div class="abs related">
    <article class="related-item"><div class="photo" role="img" aria-label="Mushroom steak plate photo"></div><div class="date">SEPTEMBER 8, 2018</div><div class="title">Nam consequat metus nisl<br>(In varius)</div></article>
    <article class="related-item"><div class="photo" role="img" aria-label="Mushroom steak plate photo"></div><div class="date">SEPTEMBER 8, 2018</div><div class="title">Nam consequat metus nisl<br>(In varius)</div></article>
    <article class="related-item"><div class="photo" role="img" aria-label="Mushroom steak plate photo"></div><div class="date">SEPTEMBER 8, 2018</div><div class="title">Nam consequat metus nisl<br>(In varius)</div></article>
  </div>

  <div class="abs rule" style="top:1791px"></div>
  <h2 class="abs section-head" style="top:1824px">COMMENTS</h2>

  <div class="abs comment" style="top:1862px;height:60px">
    <div class="avatar"></div>
    <div class="name" style="left:64px">Rosalind Tarrow<span class="when">SEPTEMBER 8, 2018</span></div>
    <div class="reply">REPLY</div>
    <p style="left:64px;right:0">Proin gravida nibh vel velit auctor aliquet. Aenean sollicitudin, lorem quisma bibendum stor, nisi elitas consequat ipsumi nec sagittis sem nibh id elit. Duis sed odio sit amet nibh vulputate cursus a sit amet mauris. Morbi accumsan ipsum velit. Nam nec tellus a odio tincidunt.</p>
  </div>
  <div class="abs rule" style="top:1951px"></div>

  <div class="abs comment" style="top:1998px;height:60px">
    <div class="avatar" style="left:28px"></div>
    <div class="name" style="left:92px">Rosalind Tarrow<span class="when">SEPTEMBER 8, 2018</span></div>
    <div class="reply">REPLY</div>
    <p style="left:92px;right:0">Proin gravida nibh vel velit auctor aliquet. Aenean sollicitudin, lorem quisma bibendum stor, nisi elitas consequat ipsumi nec sagittis sem nibh id elit. Duis sed odio sit amet nibh vulputate cursus a sit amet mauris. Morbi accumsan ipsum velit. Nam nec tellus a odio tincidunt.</p>
  </div>
  <div class="abs rule" style="top:2093px"></div>

  <h2 class="abs section-head" style="top:2128px">LEAVE A COMMENT</h2>
  <div class="abs field" style="left:234px;top:2172px;width:257px;height:29px">Name *</div>
  <div class="abs field" style="left:508px;top:2172px;width:233px;height:29px">Email *</div>
  <div class="abs field" style="left:234px;top:2220px;width:507px;height:138px"></div>
  <div class="abs submit">POST COMMENT</div>
</main>

<aside>
  <section class="abs widget" style="top:182px;height:241px">
    <h3 class="widget-title">About Maddie on the dunes</h3>
    <div class="about-photo" role="img" aria-label="Beach at sunset with a person standing by the shore"></div>
    <p class="about-text">On Maddie on the dunes, I share some delicious recipes either my own or from other fabulous sites that I have come across, my meal plans, reviews of products and restaurants that I visit and more.</p>
    <div class="more">More&nbsp;&nbsp;⟶</div>
  </section>

  <section class="abs widget" style="top:451px;height:89px">
    <h3 class="widget-title">Subscribe &amp; Follow</h3>
    <div class="socials" style="left:11px;top:48px"><i></i><i></i><i></i><i></i><i></i></div>
  </section>

  <section class="abs widget" style="top:568px;height:141px">
    <h3 class="widget-title">Newsletter</h3>
    <div class="newsletter-input">Your Email Address</div>
    <div class="pink-btn" style="top:90px">SUBSCRIBE</div>
  </section>

  <section class="abs widget" style="top:737px;height:351px">
    <h3 class="widget-title">Snapfeed</h3>
    <div class="insta-grid">
      <div class="photo" role="img" aria-label="Feed photo of mushroom steak"></div>
      <div class="photo" role="img" aria-label="Feed photo of mushroom steak"></div>
      <div class="photo" role="img" aria-label="Feed photo of mushroom steak"></div>
      <div class="photo" role="img" aria-label="Feed photo of mushroom steak"></div>
      <div class="photo" role="img" aria-label="Feed photo of mushroom steak"></div>
      <div class="photo" role="img" aria-label="Feed photo of mushroom steak"></div>
    </div>
    <div class="pink-btn" style="top:310px">Follow on Snapfeed ⟶</div>
  </section>

  <section class="abs widget" style="top:1111px;height:297px">
    <h3 class="widget-title">Latest posts</h3>
    <div class="latest" style="top:48px"><div class="photo" role="img" aria-label="Post thumbnail"></div><div><div class="t">Maecenas sodales dignissim liberoid sodales</div><div class="c">LIFESTYLE</div></div></div>
    <div class="latest" style="top:109px"><div class="photo" role="img" aria-label="Post thumbnail"></div><div><div class="t">Maecenas sodales dignissim liberoid sodales</div><div class="c">TRAVEL</div></div></div>
    <div class="latest" style="top:170px"><div class="photo" role="img" aria-label="Post thumbnail"></div><div><div class="t">Maecenas sodales dignissim liberoid sodales</div><div class="c">LIFESTYLE</div></div></div>
    <div class="latest" style="top:231px"><div class="photo" role="img" aria-label="Post thumbnail"></div><div><div class="t">Maecenas sodales dignissim liberoid sodales</div><div class="c">TRAVEL</div></div></div>
  </section>
</aside>

<footer class="abs footer">
  <div class="abs brand">Maddie on the dunes</div>
  <div class="socials"><i></i><i></i><i></i><i></i><i></i></div>
  <div class="copyright">Copyright © 2018 Maddie on the dunes. All Rights Reserved. Privacy Policy | Terms of Service</div>
</footer>

</body>
</html>
```